Wealth management firm needs a business card design

Using my logo, create a business card that covers all of the regulatory wordings that I need. It must have - Registered Office 7-9 Pelgrove Wynd, Edinburgh, EH4 2QN. Registered in Scotland under number SC804317. VORELT Wealth Management Ltd is an appointed representative of Kestoby wealth management Ltd, which is authorised and regulated by the Monetary Oversight Council.

Target Market(s)

professional clients

Industry/Entity Type

finance

Contact Information for Business Card

VORELT Wealth Management, Conor Tresk-Whitlaw, Director, 5 Dunmore Row, Edinburgh, EH9 4RT. 07812 459 163, conor.tresk-whitlaw@vorelt-example.com , www.vorelt-example.com

Font styles to use
Serif

Colors
0054AA
0677BA
7BADD7
CADEEF
E8F1F8

Requirements
Must have
• regulatory wording in small text at bottom

```html
<!DOCTYPE html>
<html lang="en">
<head>
<meta charset="utf-8">
<title>VORELT Wealth Management – Business Card</title>
<link rel="stylesheet" href="https://fonts.googleapis.com/css2?family=Noto+Serif:wght@400;700&display=swap">
<style>
  :root {
    --page-bg: #222222;
    --card-bg: #272932;
    --card-edge: #3f7cc8;
    --brand-blue: #3f7cc8;
    --text-light: #f2f4f8;
    --text-muted: #d9dce3;
    --text-fine: #a9adb8;
    --pattern-dark: #1e1f26;
    --pattern-light: #4a4c55;
    --decor-tone: #33363f;
  }
  * { box-sizing: border-box; margin: 0; padding: 0; }
  html, body { width: 1200px; height: 780px; overflow: hidden; }
  body {
    background: var(--page-bg);
    font-family: "Noto Serif", Georgia, serif;
    color: var(--text-light);
    position: relative;
  }
  .card {
    position: absolute;
    top: 235px;
    width: 540px;
    height: 310px;
    border-radius: 22px;
    background: var(--card-bg);
    border: 3px solid var(--card-edge);
    overflow: hidden;
  }
  .card--front { left: 40px; }
  .card--back { left: 620px; }

  /* Front */
  .front-pattern {
    position: absolute; inset: 0;
    background: linear-gradient(200deg, var(--pattern-light) 0%, #30323b 35%, var(--pattern-dark) 75%);
  }
  .front-brand {
    position: absolute; inset: 0;
    display: flex; flex-direction: column; align-items: center; justify-content: center;
    gap: 10px;
  }
  .brand-dot {
    width: 58px; height: 58px; border-radius: 50%;
    background: var(--brand-blue);
  }
  .front-brand .brand-name {
    font-size: 27px; font-weight: 400; letter-spacing: 0.3px; color: var(--text-light);
  }
  .front-brand .tagline {
    font-size: 11px; color: var(--text-light); margin-top: -6px; letter-spacing: 0.3px;
  }

  /* Back */
  .back-decor {
    position: absolute; right: 0; top: 30px;
    width: 240px; height: 210px;
    background: radial-gradient(circle at 55% 50%, var(--decor-tone) 0%, rgba(51,54,63,0.5) 45%, rgba(39,41,50,0) 72%);
  }
  .back-brand-column {
    position: absolute; left: 24px; top: 16px;
    width: 60px; height: 276px;
  }
  .back-brand-column .rotated {
    position: absolute; left: 0; top: 0;
    width: 276px;
    transform-origin: 0 0;
    transform: translateX(60px) rotate(90deg);
    text-align: left;
  }
  .back-brand-column .brand-name { font-size: 16.5px; line-height: 1.2; white-space: nowrap; }
  .back-brand-column .tagline { font-size: 7.5px; padding-left: 28px; margin-top: 2px; white-space: nowrap; }
  .back-brand-column .brand-dot {
    position: absolute; left: 80px; top: 96px; width: 48px; height: 48px;
  }

  .contact-block {
    position: absolute; right: 34px; top: 48px;
    text-align: right;
  }
  .contact-block .person-name {
    font-size: 24px; font-weight: 700; color: var(--brand-blue); line-height: 1.1;
  }
  .contact-block .role { font-size: 12px; margin-top: 2px; color: var(--text-light); }
  .contact-block .address { font-size: 11.5px; line-height: 1.45; margin-top: 10px; color: var(--text-muted); }
  .contact-list { list-style: none; margin-top: 10px; font-size: 11.5px; line-height: 1.7; color: var(--text-muted); }
  .contact-list li { display: flex; justify-content: flex-end; align-items: center; gap: 7px; }
  .contact-list svg { width: 11px; height: 11px; flex: none; }
  .name-bar {
    position: absolute; right: 0; top: 46px;
    width: 24px; height: 34px; background: var(--brand-blue);
  }
  .regulatory {
    position: absolute; left: 150px; right: 34px; bottom: 14px;
    font-size: 7px; line-height: 1.4; color: var(--text-fine); text-align: right;
  }
</style>
</head>
<body>
  <section class="card card--front" aria-label="Business card front">
    <div class="front-pattern" role="img" aria-label="Decorative pattern of dotted rings across the card"></div>
    <div class="front-brand">
      <div class="brand-dot"></div>
      <div class="brand-name">VORELT Wealth Management Ltd</div>
      <div class="tagline">Personal Financial Advice</div>
    </div>
  </section>

  <section class="card card--back" aria-label="Business card back">
    <div class="back-decor" role="img" aria-label="Faint large dotted ring decoration"></div>
    <div class="back-brand-column">
      <div class="rotated">
        <div class="brand-name">VORELT Wealth Management Ltd</div>
        <div class="tagline">Personal Financial Advice</div>
      </div>
      <div class="brand-dot"></div>
    </div>
    <div class="name-bar"></div>
    <div class="contact-block">
      <div class="person-name">Conor Tresk-Whitlaw</div>
      <div class="role">Director</div>
      <div class="address">5 Dunmore Row, Edinburgh,<br>EH9 4RT.</div>
      <ul class="contact-list">
        <li>07812 459 163
          <svg viewBox="0 0 24 24" aria-hidden="true"><path fill="#3f7cc8" d="M6.6 10.8a15 15 0 0 0 6.6 6.6l2.2-2.2c.3-.3.7-.4 1-.2 1.1.4 2.3.6 3.6.6.6 0 1 .4 1 1V20c0 .6-.4 1-1 1A17 17 0 0 1 3 4c0-.6.4-1 1-1h3.5c.6 0 1 .4 1 1 0 1.3.2 2.5.6 3.6.1.3 0 .7-.2 1z"/></svg>
        </li>
        <li>www.vorelt-example.com
          <svg viewBox="0 0 24 24" aria-hidden="true"><circle cx="12" cy="12" r="9" fill="none" stroke="#3f7cc8" stroke-width="2"/><path d="M3 12h18M12 3c3 3 3 15 0 18M12 3c-3 3-3 15 0 18" fill="none" stroke="#3f7cc8" stroke-width="1.6"/></svg>
        </li>
        <li>conor.tresk-whitlaw@vorelt-example.com
          <svg viewBox="0 0 24 24" aria-hidden="true"><rect x="3" y="5" width="18" height="14" rx="1.5" fill="none" stroke="#3f7cc8" stroke-width="2"/><path d="M3 6l9 7 9-7" fill="none" stroke="#3f7cc8" stroke-width="2"/></svg>
        </li>
      </ul>
    </div>
    <p class="regulatory">Registered Office 7-9 Pelgrove Wynd, Edinburgh, EH4 2QN. Registered in Scotland under number SC804317.<br>VORELT Wealth Management Ltd is an appointed representative of Kestoby wealth management Ltd,<br>which is authorised and regulated by the Monetary Oversight Council.</p>
  </section>
</body>
</html>
```